Team email banner for internal communications

We need a team email banner/header that will be applied to all internal communications from our department to other functions. The graphic should be optimized for Outlook and be landscape in layout. We have 5 different silo within our team and will need so will either need have a blank space to denote each team or have change in colors/graphics to denote each team (see current headers attached to job description). We are looking for a banner that combines our team logo (attached) with our team name, Regional Talent & Coaching Unit. The theme should be L&D and pharmaceutical in nature.

Need extra days to review

The text in the banner should be Regional Talent & Coaching Unit with the team logo (attached).

```html
<!DOCTYPE html>
<html lang="en">
<head>
<meta charset="utf-8">
<title>Regional Talent &amp; Coaching Unit – Team Email Banners</title>
<link rel="stylesheet" href="https://fonts.googleapis.com/css2?family=Montserrat:wght@500;600;700&display=swap">
<style>
  :root {
    --canvas: #ffffff;
    --panel: #f1f1f1;
    --charcoal: #3a3a3a;
    --brand-red: #d8322a;
    --hematology: #c8213a;
    --solid-tumor: #7b5aa6;
    --leadership: #2fb389;
    --market-access: #c9992f;
    --operations: #336699;
  }
  html, body {
    margin: 0;
    padding: 0;
    width: 706px;
    height: 1200px;
    overflow: hidden;
    background: var(--canvas);
  }
  .banner-stack {
    position: relative;
    width: 706px;
    height: 1200px;
  }
  .team-banner {
    position: absolute;
    left: 14px;
    width: 678px;
    height: 226px;
    font-family: "Montserrat", sans-serif;
  }
  .team-banner--hematology   { top: 14px;  --accent: var(--hematology); }
  .team-banner--solid-tumor  { top: 251px; --accent: var(--solid-tumor); }
  .team-banner--leadership   { top: 487px; --accent: var(--leadership); }
  .team-banner--market       { top: 724px; --accent: var(--market-access); }
  .team-banner--operations   { top: 960px; --accent: var(--operations); }

  .banner-art {
    position: absolute;
    inset: 0;
    width: 678px;
    height: 226px;
    display: block;
  }
  .banner-art .panel { fill: var(--panel); }
  .banner-art .charcoal { fill: var(--charcoal); }
  .banner-art .brand-red { fill: var(--brand-red); }
  .banner-art .accent-fill { fill: var(--accent); }
  .banner-art .accent-stroke { stroke: var(--accent); fill: none; }

  .identity {
    position: absolute;
    left: 97px;
    width: 300px;
    top: 0;
    text-align: center;
    color: var(--charcoal);
  }
  .identity__mark {
    position: absolute;
    top: 58px;
    left: 0;
    width: 300px;
    display: flex;
    justify-content: center;
    align-items: center;
    gap: 6px;
  }
  .identity__dot {
    width: 12px;
    height: 12px;
    border-radius: 50%;
    background: var(--brand-red);
  }
  .identity__short {
    font-weight: 700;
    font-size: 26px;
    line-height: 1;
    color: var(--charcoal);
    letter-spacing: 1px;
  }
  .identity__name {
    position: absolute;
    top: 92px;
    left: 0;
    width: 300px;
    font-weight: 600;
    font-size: 38px;
    line-height: 1;
    letter-spacing: 2.5px;
    color: var(--charcoal);
  }
  .identity__tagline {
    position: absolute;
    top: 133px;
    left: 0;
    width: 300px;
    display: flex;
    align-items: center;
    gap: 6px;
    font-weight: 500;
    font-size: 11.5px;
    line-height: 1;
    color: var(--charcoal);
    white-space: nowrap;
  }
  .identity__rule {
    flex: 1;
    height: 3px;
    background: var(--brand-red);
  }
  .team-label {
    position: absolute;
    top: 175px;
    left: 47px;
    width: 400px;
    text-align: center;
    font-family: "Montserrat", sans-serif;
    font-weight: 700;
    font-size: 21px;
    line-height: 1;
    color: var(--accent);
    white-space: nowrap;
  }
</style>
</head>
<body>
<main class="banner-stack">

  <!-- Reusable banner structure repeated per team -->
  <section class="team-banner team-banner--hematology">
    <svg class="banner-art" viewBox="0 0 960 320" aria-hidden="true">
      <rect class="panel" x="0" y="0" width="960" height="320"/>
      <polygon class="brand-red" points="0,0 150,0 133,20 0,20"/>
      <polygon class="charcoal" points="0,20 162,20 145,40 0,40"/>
      <polygon class="accent-fill" points="0,40 115,40 98,60 0,60"/>
      <polygon class="charcoal" points="0,292 730,292 760,320 0,320"/>
      <polygon class="charcoal" points="0,240 0,320 48,320"/>
      <line class="accent-stroke" x1="0" y1="205" x2="68" y2="320" stroke-width="8"/>
      <polygon class="charcoal" points="790,0 960,0 960,320 700,320 690,292"/>
      <circle class="charcoal" cx="780" cy="160" r="155"/>
      <line class="accent-stroke" x1="798" y1="0" x2="905" y2="100" stroke-width="16"/>
      <line class="accent-stroke" x1="700" y1="270" x2="760" y2="322" stroke-width="16"/>
      <circle class="panel" cx="780" cy="160" r="128"/>
      <circle class="accent-stroke" cx="780" cy="160" r="128" stroke-width="17"/>
      <rect class="accent-fill" x="935" y="75" width="40" height="170" rx="14"/>
    </svg>
    <div class="identity">
      <div class="identity__mark"><span class="identity__dot"></span><span class="identity__short">RTC</span></div>
      <div class="identity__name">REGIONAL</div>
      <div class="identity__tagline"><span class="identity__rule"></span>TALENT &amp; COACHING UNIT<span class="identity__rule"></span></div>
    </div>
    <div class="team-label">HEMATOLOGY</div>
  </section>

  <section class="team-banner team-banner--solid-tumor">
    <svg class="banner-art" viewBox="0 0 960 320" aria-hidden="true">
      <rect class="panel" x="0" y="0" width="960" height="320"/>
      <polygon class="brand-red" points="0,0 150,0 133,20 0,20"/>
      <polygon class="charcoal" points="0,20 162,20 145,40 0,40"/>
      <polygon class="accent-fill" points="0,40 115,40 98,60 0,60"/>
      <polygon class="charcoal" points="0,292 730,292 760,320 0,320"/>
      <polygon class="charcoal" points="0,240 0,320 48,320"/>
      <line class="accent-stroke" x1="0" y1="205" x2="68" y2="320" stroke-width="8"/>
      <polygon class="charcoal" points="790,0 960,0 960,320 700,320 690,292"/>
      <circle class="charcoal" cx="780" cy="160" r="155"/>
      <line class="accent-stroke" x1="798" y1="0" x2="905" y2="100" stroke-width="16"/>
      <line class="accent-stroke" x1="700" y1="270" x2="760" y2="322" stroke-width="16"/>
      <circle class="panel" cx="780" cy="160" r="128"/>
      <circle class="accent-stroke" cx="780" cy="160" r="128" stroke-width="17"/>
      <rect class="accent-fill" x="935" y="75" width="40" height="170" rx="14"/>
    </svg>
    <div class="identity">
      <div class="identity__mark"><span class="identity__dot"></span><span class="identity__short">RTC</span></div>
      <div class="identity__name">REGIONAL</div>
      <div class="identity__tagline"><span class="identity__rule"></span>TALENT &amp; COACHING UNIT<span class="identity__rule"></span></div>
    </div>
    <div class="team-label">SOLID TUMOR</div>
  </section>

  <section class="team-banner team-banner--leadership">
    <svg class="banner-art" viewBox="0 0 960 320" aria-hidden="true">
      <rect class="panel" x="0" y="0" width="960" height="320"/>
      <polygon class="brand-red" points="0,0 150,0 133,20 0,20"/>
      <polygon class="charcoal" points="0,20 162,20 145,40 0,40"/>
      <polygon class="accent-fill" points="0,40 115,40 98,60 0,60"/>
      <polygon class="charcoal" points="0,292 730,292 760,320 0,320"/>
      <polygon class="charcoal" points="0,240 0,320 48,320"/>
      <line class="accent-stroke" x1="0" y1="205" x2="68" y2="320" stroke-width="8"/>
      <polygon class="charcoal" points="790,0 960,0 960,320 700,320 690,292"/>
      <circle class="charcoal" cx="780" cy="160" r="155"/>
      <line class="accent-stroke" x1="798" y1="0" x2="905" y2="100" stroke-width="16"/>
      <line class="accent-stroke" x1="700" y1="270" x2="760" y2="322" stroke-width="16"/>
      <circle class="panel" cx="780" cy="160" r="128"/>
      <circle class="accent-stroke" cx="780" cy="160" r="128" stroke-width="17"/>
      <rect class="accent-fill" x="935" y="75" width="40" height="170" rx="14"/>
    </svg>
    <div class="identity">
      <div class="identity__mark"><span class="identity__dot"></span><span class="identity__short">RTC</span></div>
      <div class="identity__name">REGIONAL</div>
      <div class="identity__tagline"><span class="identity__rule"></span>TALENT &amp; COACHING UNIT<span class="identity__rule"></span></div>
    </div>
    <div class="team-label">LEADERSHIP DEVELOPMENT</div>
  </section>

  <section class="team-banner team-banner--market">
    <svg class="banner-art" viewBox="0 0 960 320" aria-hidden="true">
      <rect class="panel" x="0" y="0" width="960" height="320"/>
      <polygon class="brand-red" points="0,0 150,0 133,20 0,20"/>
      <polygon class="charcoal" points="0,20 162,20 145,40 0,40"/>
      <polygon class="accent-fill" points="0,40 115,40 98,60 0,60"/>
      <polygon class="charcoal" points="0,292 730,292 760,320 0,320"/>
      <polygon class="charcoal" points="0,240 0,320 48,320"/>
      <line class="accent-stroke" x1="0" y1="205" x2="68" y2="320" stroke-width="8"/>
      <polygon class="charcoal" points="790,0 960,0 960,320 700,320 690,292"/>
      <circle class="charcoal" cx="780" cy="160" r="155"/>
      <line class="accent-stroke" x1="798" y1="0" x2="905" y2="100" stroke-width="16"/>
      <line class="accent-stroke" x1="700" y1="270" x2="760" y2="322" stroke-width="16"/>
      <circle class="panel" cx="780" cy="160" r="128"/>
      <circle class="accent-stroke" cx="780" cy="160" r="128" stroke-width="17"/>
      <rect class="accent-fill" x="935" y="75" width="40" height="170" rx="14"/>
    </svg>
    <div class="identity">
      <div class="identity__mark"><span class="identity__dot"></span><span class="identity__short">RTC</span></div>
      <div class="identity__name">REGIONAL</div>
      <div class="identity__tagline"><span class="identity__rule"></span>TALENT &amp; COACHING UNIT<span class="identity__rule"></span></div>
    </div>
    <div class="team-label">MARKET ACCESS</div>
  </section>

  <section class="team-banner team-banner--operations">
    <svg class="banner-art" viewBox="0 0 960 320" aria-hidden="true">
      <rect class="panel" x="0" y="0" width="960" height="320"/>
      <polygon class="brand-red" points="0,0 150,0 133,20 0,20"/>
      <polygon class="charcoal" points="0,20 162,20 145,40 0,40"/>
      <polygon class="accent-fill" points="0,40 115,40 98,60 0,60"/>
      <polygon class="charcoal" points="0,292 730,292 760,320 0,320"/>
      <polygon class="charcoal" points="0,240 0,320 48,320"/>
      <line class="accent-stroke" x1="0" y1="205" x2="68" y2="320" stroke-width="8"/>
      <polygon class="charcoal" points="790,0 960,0 960,320 700,320 690,292"/>
      <circle class="charcoal" cx="780" cy="160" r="155"/>
      <line class="accent-stroke" x1="798" y1="0" x2="905" y2="100" stroke-width="16"/>
      <line class="accent-stroke" x1="700" y1="270" x2="760" y2="322" stroke-width="16"/>
      <circle class="panel" cx="780" cy="160" r="128"/>
      <circle class="accent-stroke" cx="780" cy="160" r="128" stroke-width="17"/>
      <rect class="accent-fill" x="935" y="75" width="40" height="170" rx="14"/>
    </svg>
    <div class="identity">
      <div class="identity__mark"><span class="identity__dot"></span><span class="identity__short">RTC</span></div>
      <div class="identity__name">REGIONAL</div>
      <div class="identity__tagline"><span class="identity__rule"></span>TALENT &amp; COACHING UNIT<span class="identity__rule"></span></div>
    </div>
    <div class="team-label">OPERATIONS &amp; CAPABILITIES</div>
  </section>

</main>
</body>
</html>
```